Hollow Meridian Book website design.

This is a simple one-page web design for my book.
I have all files and video needed.
Domain listed with Net Harbor.
Password and username will be given to winning bid.
Domain address, www.hollowmeridian.info
Upload a 30 second video so it can be played on the website.
Book cover photo
Book Blurb text.
Links to Brightcart and Audio books where the book can be purchased.
Below is the link to the Brightcart listing.
https://www.brightcart.example/dp/X47QTRWLM2/?coliid=PLKWEZNRTBQVS&colid=9HRTUQWBNLKC4&psc=0&ref_=lv_ov_lig_dp_i
Below is the link to my Earshelf books.com listing.
https://www.earshelf.example/pd/Hollow-Meridian-Audiobook/X82LMQTVR3?qid=5093718264&sr=1-7&ref=a_search_c3_lProduct_1_7&pf_rd_p=47a91bde-e517-4c3a-9d0e-61b3fa2c8d7e&pf_rd_r=QWPLRTZKX52NBMVH8DJS
Text on page.” Click on either logo to go directly to Brightcart or Earshelf.com
Link Earshelf book logo to my book on Earshelf.com
Place this text under Earshelf.com logo: “Free to new members of Earshelf.com”
Link Brightcart logo to my book on Brightcart.
Place this text under Brightcart logo “ Free to new Pagewisp members on Brightcart.com”
Link the book photo to the Brightcart.com web address as well.
Enter meta tags or keywords below for search engines to locate webpage.
Hollow Meridian
Conspiracy
Conspiracy Books
Spy books
Thriller books
Suspense books
Comedy books
Warren Ostby

```html
<!DOCTYPE html>
<html lang="en">
<head>
<meta charset="utf-8">
<title>Hollow Meridian</title>
<meta name="keywords" content="Hollow Meridian, Conspiracy, Conspiracy Books, Spy books, Thriller books, Suspense books, Comedy books, Warren Ostby">
<link rel="stylesheet" href="https://fonts.googleapis.com/css2?family=Poppins:wght@400;600;700&family=Roboto:wght@300;400&display=swap">
<style>
:root{
  --orange:#f0861b;
  --ink:#2a2a2e;
  --text:#3b3b40;
  --white:#ffffff;
  --footer:#07070b;
  --hero-top:#2a3448;
  --hero-mid:#7a3a3a;
  --hero-low:#3a1a1a;
}
*{box-sizing:border-box;margin:0;padding:0}
html,body{width:904px;height:1200px;overflow:hidden}
body{position:relative;background:var(--footer);font-family:'Roboto',sans-serif;color:var(--text)}
.hero{position:absolute;left:0;top:0;width:904px;height:517px;
  background:
    radial-gradient(ellipse at 90% 45%,rgba(240,110,40,.75),transparent 45%),
    radial-gradient(ellipse at 5% 40%,rgba(190,40,50,.65),transparent 40%),
    linear-gradient(180deg,#2c3346 0%,#4b4656 35%,#8a4234 62%,#5a1f1f 80%,#2b1a18 100%)}
.brand{position:absolute;left:83px;top:18px;font-family:'Poppins',sans-serif;font-size:21px;color:var(--white);font-weight:400;letter-spacing:.2px}
.brand b{font-weight:700}
.menu{position:absolute;left:803px;top:22px}
.video{position:absolute;left:164px;top:139px;width:576px;height:315px;
  background:radial-gradient(ellipse at 50% 45%,#6b6660,#2d3138 55%,#1a1e26 100%)}
.play{position:absolute;left:423px;top:268px}
.watch{position:absolute;left:0;width:904px;top:341px;text-align:center;font-family:'Poppins',sans-serif;font-size:11px;color:var(--white)}
.watch span{border-bottom:1px solid var(--white);padding-bottom:1px}
.books{position:absolute;top:517px;left:0;width:904px;height:390px;display:flex}
.book{position:relative;width:452px;height:390px;background:linear-gradient(90deg,#adadb0 0%,#d6d6d8 50%,#e6e6e8 100%)}
.cover{position:absolute;left:38px;top:36px;width:152px;height:226px;border-radius:3px 6px 6px 3px;
  background:linear-gradient(135deg,#1c2340 0%,#6a1820 40%,#111 70%,#2a2a2a 100%);box-shadow:4px 6px 10px rgba(0,0,0,.35)}
.info{position:absolute;left:214px;top:36px;width:206px}
.title{font-family:'Poppins',sans-serif;font-weight:600;font-size:16.5px;line-height:22px;color:var(--ink);height:54px}
.offer{margin-top:4px;font-family:'Poppins',sans-serif;font-weight:600;font-size:12.5px;line-height:16px;color:var(--ink)}
.offer em{font-style:normal;color:var(--orange)}
.blurb{margin-top:13px;font-size:10.3px;line-height:16.2px;text-align:justify;font-weight:300;color:var(--text)}
.go{margin-top:21px;display:flex;align-items:center;gap:12px;font-size:10.5px;font-weight:300}
.go a{text-decoration:none;font-family:'Poppins',sans-serif;font-weight:700;font-size:19px;color:var(--ink)}
.footer{position:absolute;top:907px;left:0;width:904px;height:293px;color:var(--white)}
.col{position:absolute;top:67px}
.col h3{font-family:'Roboto',sans-serif;font-weight:400;font-size:19.5px;height:42px}
.col ul{list-style:none}
.col li{font-size:11.5px;line-height:19.4px;font-weight:300;position:relative;padding-left:20px}
.col li.chev::before{content:"›";position:absolute;left:0;top:-1px;font-size:13px}
.col li svg{position:absolute;left:0;top:5px}
.copy{position:absolute;top:237px;left:0;width:904px;text-align:center;font-size:11px;font-weight:300}
</style>
</head>
<body>
<header class="hero" role="img" aria-label="City skyline at sunset with a waving national flag">
  <div class="brand"><b>Hollow</b> Meridian</div>
  <svg class="menu" width="17" height="15" viewBox="0 0 17 15"><rect y="0" width="17" height="2.6" fill="#fff"/><rect y="6" width="17" height="2.6" fill="#fff"/><rect y="12" width="17" height="2.6" fill="#fff"/></svg>
  <div class="video" role="img" aria-label="Video still of a man in glasses resting his chin on his hand"></div>
  <svg class="play" width="58" height="58" viewBox="0 0 58 58">
    <circle cx="29" cy="29" r="29" fill="#f0861b" opacity=".45"/>
    <circle cx="29" cy="29" r="21.5" fill="#f0861b"/>
    <polygon points="26,24 34,29 26,34" fill="#fff"/>
  </svg>
  <div class="watch"><span>WATCH VIDEO</span></div>
</header>

<section class="books">
  <article class="book">
    <a class="cover" href="#" role="img" aria-label="Hollow Meridian book cover, Pagewisp edition"></a>
    <div class="info">
      <h2 class="title">Hollow Meridian<br>Pagewisp Edition</h2>
      <p class="offer">Free to new Pagewisp members<br>on <em>Brightcart.com</em></p>
      <p class="blurb">A fictional novel based on current events surrounding the covid 19 virous. Jack Holman is a well-respected independent journalist contracted by the Harbor Ledger, upon his return from reporting on the war in Syria he is tasked to investigate the covid virus outbreak in China. As he digs deeper, he uncovers a hideous plot by the powers that be here in America. Jack risks life and limb to uncover the conspirers behind all of this and shed light to the American people.</p>
      <p class="go">Click to go directly to <a href="#">Brightcart</a></p>
    </div>
  </article>
  <article class="book">
    <a class="cover" href="#" role="img" aria-label="Hollow Meridian book cover, audiobook edition"></a>
    <div class="info">
      <h2 class="title">Hollow Meridian</h2>
      <p class="offer">Free to new members of<br><em>Earshelf.com</em></p>
      <p class="blurb">A fictional novel based on current events surrounding the covid 19 virous. Jack Holman is a well-respected independent journalist contracted by the Harbor Ledger, upon his return from reporting on the war in Syria he is tasked to investigate the covid virus outbreak in China. As he digs deeper, he uncovers a hideous plot by the powers that be here in America. Jack risks life and limb to uncover the conspirers behind all of this and shed light to the American people.</p>
      <p class="go">Click to go directly to <a href="#">Earshelf</a></p>
    </div>
  </article>
</section>

<footer class="footer">
  <div class="col" style="left:122px">
    <h3>Quick links</h3>
    <ul><li class="chev">Home</li><li class="chev">About us</li><li class="chev">Blog</li><li class="chev">Reviews</li></ul>
  </div>
  <div class="col" style="left:231px;top:109px">
    <ul><li class="chev">Privacy policy</li><li class="chev">Terms &amp; condition</li><li class="chev">Support</li><li class="chev">Faq</li></ul>
  </div>
  <div class="col" style="left:412px">
    <h3>Information</h3>
    <ul><li class="chev">Contact us</li><li class="chev">About us</li><li class="chev">Privacy policy</li><li class="chev">Terms &amp; Conditions</li></ul>
  </div>
  <div class="col" style="left:599px">
    <h3>Contact us</h3>
    <ul>
      <li><svg width="10" height="10" viewBox="0 0 10 10"><path d="M2 0.5l2 2-1 1.3c.6 1.3 1.6 2.3 2.9 2.9l1.3-1 2 2-1.3 1.6C4.5 9 1 5.5.5 1.8z" fill="#f0861b"/></svg>Phone : +1 888 888 8888</li>
      <li><svg width="11" height="8" viewBox="0 0 11 8"><rect width="11" height="8" rx="1" fill="#f0861b"/><path d="M0.5 0.8L5.5 4.5 10.5 0.8" stroke="#07070b" fill="none"/></svg>Email : info@companyname.com</li>
      <li><svg width="8" height="11" viewBox="0 0 8 11"><path d="M4 0a4 4 0 0 1 4 4c0 3-4 7-4 7S0 7 0 4a4 4 0 0 1 4-4z" fill="#f0861b"/><circle cx="4" cy="4" r="1.5" fill="#07070b"/></svg>Address :</li>
      <li>Lorem ipsum dolor sit amet</li>
    </ul>
  </div>
  <p class="copy">© Copyright @2022 Company name | All Rights Reserved</p>
</footer>
</body>
</html>
```